International horse riding portal needs web design

We are looking for the web design for the new "Vosmerik" web portal.

Offers from the world of horses and riding should be found on this portal, eg from the categories riding schools, riding holidays, farriers, riding stables, riding stables. And all information about riding.

It is important that the different areas can be found easily and clearly. For some categories, some features should already be available in the search bar.

In addition, the design should make you want to go horse riding. The user should be emotionally picked up on the landing page.

In the lower area, some offers should be advertised, eg from the areas of riding holidays, riding training, and horse trading.

Please use the colors from the logo for the design.
C100 M50 Y10 K50 and C0 M20 Y60 K30

```html
<!DOCTYPE html>
<html lang="en">
<head>
<meta charset="utf-8">
<title>Vosmerik – For The Love Of Horses</title>
<link rel="stylesheet" href="https://fonts.googleapis.com/css2?family=Della+Respira&family=Didact+Gothic&display=swap">
<style>
:root{
  --navy:#003f6e;
  --navy-deep:#023a66;
  --gold:#b8975a;
  --gold-dark:#8f7448;
  --ink:#2b2b2b;
  --line:#d3d3d3;
  --white:#ffffff;
}
*{box-sizing:border-box;margin:0;padding:0}
html,body{width:1200px;height:2520px;overflow:hidden;background:var(--white)}
body{position:relative;font-family:"Didact Gothic",sans-serif;color:var(--ink)}
.abs{position:absolute}
.serif{font-family:"Della Respira",serif}

/* header */
.brand{left:60px;top:28px;width:200px;height:136px;display:flex;flex-direction:column;align-items:center;justify-content:center;gap:8px}
.brand-dot{width:62px;height:62px;border-radius:50%;background:var(--gold)}
.brand-name{font-family:"Della Respira",serif;font-size:32px;color:var(--navy);letter-spacing:1px}
.search{left:304px;top:33px;width:334px;height:36px;border-radius:18px;background:var(--gold);overflow:hidden;display:flex}
.search-field{flex:1;color:#fff;font-size:13px;padding:10px 0 0 20px}
.search-btn{width:67px;background:var(--navy);color:#fff;font-size:13px;text-align:center;padding-top:10px}
.minimenu{left:655px;top:33px;width:349px;height:36px;display:flex;border:1px solid var(--line)}
.minimenu span{flex:1;text-align:center;font-size:13px;padding-top:10px;border-right:1px solid var(--line)}
.minimenu span:last-child{border-right:0}
.login{left:1012px;top:33px;width:116px;height:36px;background:var(--navy);color:#fff;font-size:13px;text-align:center;padding-top:10px}
.cats{left:303px;width:825px;height:36px;display:flex;border:1px solid var(--line)}
.cats span{flex:1;text-align:center;font-size:13px;padding-top:10px;border-right:1px solid var(--line)}
.cats span:last-child{border-right:0}
.cats .active{background:var(--navy);color:#fff;position:relative}
.cats .active i{position:absolute;right:12px;font-style:normal}

/* hero */
.hero{left:0;top:191px;width:1200px;height:638px;background:radial-gradient(ellipse at 70% 45%,#a07c50 0%,#8f7448 55%,#94794c 100%);overflow:hidden}
.hero-photo{left:330px;top:-20px;width:740px;height:620px;background:radial-gradient(ellipse at 50% 55%,#8a4a22 0%,#7a4a2a 45%,rgba(143,116,72,0) 72%)}
.hero-mist{left:0;top:560px;width:1200px;height:78px;background:linear-gradient(to bottom,rgba(255,255,255,0),#f4f2ee 70%,#fff)}
.hero-kicker{left:76px;top:237px;color:#fff;font-size:22px}
.hero-title{left:76px;top:268px;color:#fff;font-size:62px;line-height:64px}
.btn{background:var(--navy);color:#fff;font-size:13px;text-align:center;padding-top:11px}
.hero-btn{left:79px;top:409px;width:166px;height:36px}
.dots{left:1158px;top:258px;width:16px}
.dots b{display:block;height:4px;background:var(--navy);margin-bottom:12px;width:8px}
.dots b.on{background:#fff;width:16px}

/* intro */
.intro-title{left:0;top:903px;width:1200px;text-align:center;font-size:33px;line-height:36px;color:#333}
.intro-col{top:1026px;width:350px;font-size:14.5px;line-height:16.5px;color:#222}

/* gallery */
.thumb{top:1138px;width:201px;height:199px}
.caption{top:1353px;width:201px;text-align:center;font-size:21px;color:#333}
.arrow{width:26px;height:26px;border-radius:50%;top:1228px}

/* offers */
.band{left:0;top:1500px;width:1200px;height:955px}
.card-photo{top:1482px;width:328px;height:256px}
.card-title{font-size:21px;color:#fff}
.card-rule{height:2px;width:74px;background:#fff}
.card-text{font-size:14.5px;line-height:16.5px;color:#fff;width:260px}
.card-btn{width:127px;height:36px}

/* footer */
.foot-brand{left:500px;top:2078px;width:200px;height:110px;display:flex;flex-direction:column;align-items:center;gap:6px}
.foot-brand .brand-dot{width:56px;height:56px;background:#fff}
.foot-brand .brand-name{color:#fff;font-size:28px}
.foot-icon{top:2212px;width:62px;height:62px;border-radius:50%;background:var(--gold);display:flex;align-items:center;justify-content:center}
.foot-text{top:2288px;color:#fff;font-size:13px;line-height:22px;text-align:center}
.quick{left:0;top:2350px;width:1200px;text-align:center;color:#fff;font-size:18px;letter-spacing:1px}
.quick-links{left:0;top:2381px;width:1200px;text-align:center;color:#fff;font-size:12px;word-spacing:2px}
.copyright{left:81px;top:2478px;font-size:13px;color:#333}
.copyright b{color:var(--navy)}
.social{top:2470px;width:30px;height:30px;border-radius:50%}
</style>
</head>
<body>

<header>
  <div class="abs brand"><span class="brand-dot"></span><span class="brand-name">VOSMERIK</span></div>
  <div class="abs search"><span class="search-field">Search &gt; Feature</span><span class="search-btn">Find</span></div>
  <nav class="abs minimenu"><span>MiniMenu</span><span>MiniMenu</span><span>My List</span></nav>
  <div class="abs login">Login</div>
  <nav class="abs cats" style="top:92px"><span class="active">Category 1 <i>v</i></span><span>Category 2</span><span>Category 3</span><span>Category 4</span><span>Category 5</span></nav>
  <nav class="abs cats" style="top:128px"><span>Category 6</span><span>Category 7</span><span>Category 8</span><span>Category 9</span><span>Category 10</span><span>Category 11</span><span>Category 12</span></nav>
</header>

<section class="abs hero">
  <div class="abs hero-photo" role="img" aria-label="Rider in navy jacket and helmet on a chestnut horse jumping"></div>
  <div class="abs hero-mist"></div>
  <div class="abs hero-kicker serif">VOSMERIK</div>
  <h1 class="abs hero-title serif" style="font-weight:400">For The Love<br>Of Horses.</h1>
  <div class="abs btn hero-btn">Rad More</div>
  <div class="abs dots"><b></b><b class="on"></b><b></b><b></b></div>
</section>

<section>
  <h2 class="abs intro-title serif" style="font-weight:400">Ihic tectio blab incienis aut hiliquo quisqui aeprectur?<br>aUresequod qui ditis</h2>
  <p class="abs intro-col" style="left:240px">Udi officipsamus dolut alicimillam fugit faceseq uodisquati suntemod eum id ut ullatquam aceat. Ibus. Dus. Erferup tatemo exererum, eum voloren</p>
  <p class="abs intro-col" style="left:630px">Udi officipsamus dolut alicimillam fugit faceseq uodisquati suntemod eum id ut ullatquam aceat. Ibus. Dus. Erferup tatemo exererum, eum voloren</p>
</section>

<section>
  <div class="abs thumb" style="left:79px;background:linear-gradient(#b9d3ea,#7f8a7d 55%,#6f9a45)" role="img" aria-label="Rider jumping a fence at a riding school"></div>
  <div class="abs thumb" style="left:291px;background:linear-gradient(135deg,#9a8a78,#5a3a2e 60%,#c2a88a)" role="img" aria-label="Woman standing beside a grey horse"></div>
  <div class="abs thumb" style="left:503px;background:radial-gradient(circle at 55% 45%,#8a7a5e,#2c2a22 70%)" role="img" aria-label="Farrier working on a horse hoof"></div>
  <div class="abs thumb" style="left:715px;background:linear-gradient(90deg,#6e4528,#3a2a22 50%,#b8b0a6)" role="img" aria-label="Smiling woman in cowboy hat with a horse"></div>
  <div class="abs thumb" style="left:927px;background:linear-gradient(90deg,#c8b08a,#3a2a22 70%,#1e1712)" role="img" aria-label="Woman nuzzling a dark horse"></div>
  <svg class="abs arrow" style="left:67px" viewBox="0 0 26 26"><circle cx="13" cy="13" r="13" fill="#b8975a"/><path d="M18 13H8M12 9l-4 4 4 4" stroke="#fff" stroke-width="1.6" fill="none"/></svg>
  <svg class="abs arrow" style="left:1114px" viewBox="0 0 26 26"><circle cx="13" cy="13" r="13" fill="#003f6e"/><path d="M8 13h10M14 9l4 4-4 4" stroke="#fff" stroke-width="1.6" fill="none"/></svg>
  <div class="abs caption serif" style="left:75px">Riding Schools</div>
  <div class="abs caption serif" style="left:287px">Riding Holidays</div>
  <div class="abs caption serif" style="left:499px">Farriers</div>
  <div class="abs caption serif" style="left:715px">Riding Stables</div>
  <div class="abs caption serif" style="left:933px">Riding Stables</div>
</section>

<section>
  <svg class="abs band" viewBox="0 0 1200 955" preserveAspectRatio="none"><polygon points="0,236 1200,88 1200,955 0,955" fill="#003f6e"/></svg>
  <div class="abs" style="left:0;top:2100px;width:420px;height:355px;background:radial-gradient(ellipse at 40% 50%,rgba(255,255,255,0.06),rgba(0,0,0,0) 70%)" role="img" aria-label="Faint silhouette of a rider on horseback"></div>

  <div class="abs card-photo" style="left:78px;background:linear-gradient(#4b6b3a,#7f8f5e 60%,#9a6a3a)" role="img" aria-label="Rider in navy shirt on a bay horse"></div>
  <div class="abs card-photo" style="left:439px;background:linear-gradient(#cfcac4,#7a6a58 55%,#4a3426)" role="img" aria-label="Rider in sunglasses on a brown horse by stables"></div>
  <div class="abs card-photo" style="left:800px;background:linear-gradient(#3e5e36,#6e7f48 50%,#b5763a)" role="img" aria-label="Rider in black on a chestnut horse in a field"></div>

  <svg class="abs" style="left:78px;top:1738px" width="328" height="260" viewBox="0 0 328 260"><polygon points="0,0 328,0 328,201 0,260" fill="#b8975a"/></svg>
  <svg class="abs" style="left:439px;top:1738px" width="329" height="260" viewBox="0 0 329 260"><polygon points="0,0 329,0 329,201 0,260" fill="#b8975a"/></svg>
  <svg class="abs" style="left:800px;top:1738px" width="328" height="260" viewBox="0 0 328 260"><polygon points="0,0 328,0 328,201 0,260" fill="#b8975a"/></svg>

  <div class="abs card-title serif" style="left:110px;top:1759px">Heading Title 01</div>
  <div class="abs card-rule" style="left:110px;top:1792px"></div>
  <p class="abs card-text" style="left:112px;top:1816px">Udi officipsamus dolut alicimillam fugit faceseq uodisquati suntemod eum id ut ullatquam aceat.</p>
  <div class="abs btn card-btn" style="left:115px;top:1894px">Rad More</div>

  <div class="abs card-title serif" style="left:474px;top:1759px">Heading Title 01</div>
  <div class="abs card-rule" style="left:474px;top:1792px"></div>
  <p class="abs card-text" style="left:476px;top:1816px">Udi officipsamus dolut alicimillam fugit faceseq uodisquati suntemod eum id ut ullatquam aceat.</p>
  <div class="abs btn card-btn" style="left:476px;top:1894px">Rad More</div>

  <div class="abs card-title serif" style="left:837px;top:1759px">Heading Title 01</div>
  <div class="abs card-rule" style="left:837px;top:1792px"></div>
  <p class="abs card-text" style="left:839px;top:1816px">Udi officipsamus dolut alicimillam fugit faceseq uodisquati suntemod eum id ut ullatquam aceat.</p>
  <div class="abs btn card-btn" style="left:840px;top:1894px">Rad More</div>
</section>

<footer>
  <div class="abs brand foot-brand"><span class="brand-dot"></span><span class="brand-name">VOSMERIK</span></div>

  <div class="abs foot-icon" style="left:354px"><svg width="24" height="24" viewBox="0 0 24 24"><path d="M6.6 10.8a15 15 0 0 0 6.6 6.6l2.2-2.2c.3-.3.7-.4 1-.2 1.1.4 2.3.6 3.6.6.6 0 1 .4 1 1V20c0 .6-.4 1-1 1A17 17 0 0 1 3 4c0-.6.4-1 1-1h3.5c.6 0 1 .4 1 1 0 1.3.2 2.5.6 3.6.1.3 0 .7-.2 1z" fill="#fff"/></svg></div>
  <div class="abs foot-icon" style="left:570px"><svg width="22" height="24" viewBox="0 0 22 24"><path d="M11 1a8 8 0 0 0-8 8c0 6 8 14 8 14s8-8 8-14a8 8 0 0 0-8-8zm0 11a3 3 0 1 1 0-6 3 3 0 0 1 0 6z" fill="#fff"/></svg></div>
  <div class="abs foot-icon" style="left:804px"><svg width="28" height="20" viewBox="0 0 28 20"><rect x="1" y="1" width="26" height="18" fill="#fff"/><path d="M1 1l13 10L27 1" stroke="#b8975a" stroke-width="1.6" fill="none"/></svg></div>

  <div class="abs foot-text" style="left:326px;width:120px">(00) 555 010 247</div>
  <div class="abs foot-text" style="left:480px;width:242px">48 Meadow Lane, Hollowbrook, Vermont<br>05001, United States</div>
  <div class="abs foot-text" style="left:742px;width:140px">info@vosmerik.com</div>

  <div class="abs quick">QUICK LINKS</div>
  <div class="abs quick-links">MiniMenu &nbsp;&nbsp;&nbsp; | &nbsp;&nbsp;&nbsp; MiniMenu &nbsp;&nbsp;&nbsp; | &nbsp;&nbsp;&nbsp; My List &nbsp;&nbsp;&nbsp; | &nbsp;&nbsp;&nbsp; Login</div>

  <div class="abs copyright">Copyright © 2022 <b>VOSMERIK</b>. All Rights Reserved.</div>
  <span class="abs social" style="left:977px;background:var(--gold)"></span>
  <span class="abs social" style="left:1018px;background:var(--navy)"></span>
  <span class="abs social" style="left:1058px;background:var(--navy)"></span>
  <span class="abs social" style="left:1098px;background:var(--navy)"></span>
</footer>

</body>
</html>
```